Prospectus/Brochure Design for Partnerships Proposal

Require prospectus to be designed for partnerships packages with our company. The goal of this prospectus is to inspire partners to join Vintrel (our company).

Design should be creative and include colour and visual elements to make engaging.

Creativity with layout is encouraged as you see fit.

Company is Vintrel.com.au

Contents of brocuhure/prospectus in .pdf. Layout ok to play around with.

Target Market(s)

Startup, Small Business

Industry/Entity Type

Startup

Font styles to use
Sans Serif

Colors

Designer to choose colors to be used in the design.

Requirements
Must have
• Well designed, colour, visual elements, consistency through design with regards to spacing, typography and design elements
Should not have
• Too many colours, select a creative colour pallete and stick with it. Clipart or non vector images.

```html
<!DOCTYPE html>
<html lang="en">
<head>
<meta charset="utf-8">
<title>Vintrel Prospectus</title>
<link rel="stylesheet" href="https://fonts.googleapis.com/css2?family=Open+Sans:wght@400;700;800&display=swap">
<style>
  :root {
    --paper: #ffffff;
    --ink: #231f20;
    --ink-soft: #333333;
    --rule: #c9c9c9;
    --photo-light: #efe6dc;
    --photo-mid: #c9b39a;
    --photo-deep: #8c735c;
  }
  * { margin: 0; padding: 0; box-sizing: border-box; }
  html, body {
    width: 900px;
    height: 1200px;
    overflow: hidden;
    background: var(--paper);
  }
  .cover {
    position: relative;
    width: 900px;
    height: 1200px;
    background: var(--paper);
    font-family: "Open Sans", Arial, sans-serif;
    color: var(--ink);
  }
  .cover__imagery {
    position: absolute;
    inset: 0;
    width: 900px;
    height: 1200px;
  }
  .brand {
    position: absolute;
    left: 75px;
    top: 520px;
    width: 480px;
  }
  .brand__name {
    font-weight: 800;
    font-size: 128px;
    line-height: 1;
    letter-spacing: -3px;
    color: var(--ink);
  }
  .brand__tagline {
    margin-top: 4px;
    text-align: right;
    font-size: 18px;
    font-weight: 400;
    color: var(--ink-soft);
    padding-right: 0;
  }
  .cover__intro {
    position: absolute;
    left: 77px;
    top: 722px;
    font-size: 24px;
    line-height: 1.32;
    font-weight: 400;
    color: var(--ink);
  }
  .cover__title {
    position: absolute;
    left: 82px;
    top: 972px;
    font-size: 58px;
    font-weight: 700;
    line-height: 1.2;
    color: var(--ink);
  }
  .cover__rule {
    position: absolute;
    left: 0;
    top: 1063px;
    width: 900px;
    height: 1px;
    background: var(--rule);
  }
  .cover__url {
    position: absolute;
    left: 0;
    top: 1103px;
    width: 900px;
    text-align: center;
    font-size: 16px;
    color: var(--ink-soft);
  }
</style>
</head>
<body>
  <main class="cover">
    <svg class="cover__imagery" viewBox="0 0 900 1200" xmlns="http://www.w3.org/2000/svg">
      <defs>
        <linearGradient id="meeting-tones" x1="0" y1="0" x2="1" y2="1">
          <stop offset="0" stop-color="var(--photo-light)"/>
          <stop offset="0.55" stop-color="var(--photo-mid)"/>
          <stop offset="1" stop-color="var(--photo-deep)"/>
        </linearGradient>
        <linearGradient id="listening-tones" x1="0" y1="0" x2="1" y2="1">
          <stop offset="0" stop-color="var(--photo-light)"/>
          <stop offset="0.6" stop-color="var(--photo-mid)"/>
          <stop offset="1" stop-color="var(--photo-deep)"/>
        </linearGradient>
      </defs>
      <polygon class="photo photo--handshake" role="img"
               aria-label="Photo of business partners shaking hands across a meeting table"
               points="223,0 667,0 526,433 67,433" fill="url(#meeting-tones)"/>
      <polygon class="photo photo--meeting" role="img"
               aria-label="Photo of a smiling woman listening in a meeting"
               points="684,629 900,629 900,1063 567,1063" fill="url(#listening-tones)"/>
    </svg>

    <header class="brand">
      <div class="brand__name">Vintrel</div>
      <p class="brand__tagline">empower. achieve. succeed.</p>
    </header>

    <p class="cover__intro">a co-working space for entrepreneurs<br>and start-up businesses in Sydney, Australia.<br>Since 2011</p>

    <h1 class="cover__title">Prospectus</h1>

    <div class="cover__rule"></div>
    <p class="cover__url">www.vintrel.com.au</p>
  </main>
</body>
</html>
```